Business Card Design for Animal Clinic

We are seeking a two sided business card design. The primary side should include our logo (provided in AI and EPS files) address, phone, website, and if possible "Follow Us" with icons for Petbook, Pawnet, and Chirper.

The back of the card needs to included space for appointment reminders.

Company Name:
Calderbrook Animal Clinic

Doctor Name:
To be provided to winner

Adress:
To be provided to winner

Phone:
to be provided to winner

Website:
www.calderbrookanimalclinic.com

```html
<!DOCTYPE html>
<html lang="en">
<head>
<meta charset="utf-8">
<title>Calderbrook Animal Clinic – Business Card</title>
<link rel="stylesheet" href="https://fonts.googleapis.com/css2?family=Questrial&display=swap">
<style>
  :root {
    --page: #ffffff;
    --peach-core: #fbbf98;
    --peach-edge: #fddcc6;
    --ink: #a5141b;
    --ink-soft: #b8503f;
    --frame: #ffffff;
    --dot-a: #c0282c;
    --dot-b: #3f8ee0;
    --dot-c: #40c2d2;
  }
  * { margin: 0; padding: 0; box-sizing: border-box; }
  html, body {
    width: 1091px; height: 1200px; overflow: hidden;
    background: var(--page);
    font-family: "Questrial", "Century Gothic", sans-serif;
    color: var(--ink);
  }
  .canvas { position: relative; width: 1091px; height: 1200px; }
  .card {
    position: absolute; left: 62px; width: 969px; height: 552px;
    background: radial-gradient(ellipse at 52% 48%, var(--peach-core) 0%, var(--peach-edge) 100%);
    overflow: hidden;
  }
  .card--front { top: 35px; }
  .card--back { top: 607px; }
  .card__frame { position: absolute; inset: 0; width: 969px; height: 552px; }
  .card__frame line { stroke: var(--frame); stroke-width: 1.6; }
  .card__frame .thin { stroke-width: 1; opacity: .8; }
  .card__frame circle { fill: var(--frame); }
  .abs { position: absolute; white-space: nowrap; }
  .centered { transform: translateX(-50%); text-align: center; }

  .brand-name { left: 484px; top: 72px; font-size: 54px; letter-spacing: 2px; }
  .brand-sub { left: 484px; top: 168px; font-size: 28px; letter-spacing: 2px; color: var(--ink-soft); display: flex; align-items: center; gap: 18px; }
  .brand-sub .mark { width: 30px; height: 30px; border-radius: 50%; background: var(--ink); display: inline-block; }
  .doctor { left: 498px; top: 292px; font-size: 41px; }
  .contact { left: 321px; font-size: 28px; }
  .contact--addr { top: 398px; }
  .contact--addr2 { top: 437px; left: 438px; }
  .contact--phone { top: 477px; }
  .website { left: 520px; top: 522px; font-size: 30px; }

  .back-title { left: 487px; top: 52px; font-size: 44px; }
  .back-lead { left: 470px; top: 116px; font-size: 30px; }
  .field { left: 138px; font-size: 30px; }
  .field--day { top: 198px; }
  .field--time { top: 247px; }
  .field--note { top: 292px; }
  .rule { position: absolute; height: 2px; background: var(--ink); }
  .notice { left: 516px; top: 376px; font-size: 26px; line-height: 34px; }

  .follow { position: absolute; left: 880px; top: 122px; width: 40px; display: flex; flex-direction: column; align-items: center; gap: 22px; }
  .follow__item { width: 40px; height: 40px; border-radius: 50%; }
  .follow__item--a { background: var(--dot-a); border-radius: 4px; }
  .follow__item--b { background: var(--dot-b); }
  .follow__item--c { background: var(--dot-c); }
  .follow__label { position: absolute; left: 900px; top: 361px; transform: translate(-50%, -50%) rotate(-90deg); font-size: 24px; white-space: nowrap; }
  .sr { position: absolute; width: 1px; height: 1px; overflow: hidden; clip: rect(0 0 0 0); }
</style>
</head>
<body>
<main class="canvas">

  <section class="card card--front" aria-label="Card front">
    <svg class="card__frame" viewBox="0 0 969 552" aria-hidden="true">
      <line class="thin" x1="100" y1="41" x2="100" y2="510"/>
      <line x1="119" y1="41" x2="119" y2="510"/>
      <line class="thin" x1="135" y1="90" x2="135" y2="420"/>
      <circle cx="119" cy="41" r="4"/><circle cx="119" cy="510" r="4"/>
      <line class="thin" x1="874" y1="41" x2="874" y2="510"/>
      <line x1="857" y1="41" x2="857" y2="510"/>
      <line class="thin" x1="843" y1="90" x2="843" y2="420"/>
      <circle cx="857" cy="41" r="4"/><circle cx="857" cy="510" r="4"/>
    </svg>
    <div class="abs centered brand-name">CALDERBROOK</div>
    <div class="abs centered brand-sub">ANIMAL <span class="mark" aria-hidden="true"></span> CLINIC</div>
    <div class="abs centered doctor">Dr. Lorem Ipsum</div>
    <div class="abs contact contact--addr">Adress: Lorem ipsum 25</div>
    <div class="abs contact contact--addr2">2100 Lorem ipsum</div>
    <div class="abs contact contact--phone">Phone: 00000055555</div>
    <div class="abs centered website">www.calderbrookanimalclinic.com</div>
  </section>

  <section class="card card--back" aria-label="Card back, appointment reminder">
    <svg class="card__frame" viewBox="0 0 969 552" aria-hidden="true">
      <line class="thin" x1="72" y1="61" x2="72" y2="528"/>
      <line x1="87" y1="61" x2="87" y2="528"/>
      <line class="thin" x1="99" y1="110" x2="99" y2="487"/>
      <circle cx="87" cy="61" r="4"/>
      <line class="thin" x1="140" y1="459" x2="830" y2="459"/>
      <line x1="69" y1="473" x2="908" y2="473"/>
      <line class="thin" x1="69" y1="487" x2="908" y2="487"/>
      <circle cx="69" cy="473" r="4"/>
    </svg>
    <div class="abs centered back-title">Calderbrook Animal Clinic</div>
    <div class="abs centered back-lead">Your next appointment is</div>
    <div class="abs field field--day">Day / Date</div>
    <div class="rule" style="left:329px; top:226px; width:510px;"></div>
    <div class="abs field field--time">Time</div>
    <div class="rule" style="left:220px; top:272px; width:619px;"></div>
    <div class="abs field field--note">Note</div>
    <div class="rule" style="left:220px; top:318px; width:619px;"></div>
    <div class="rule" style="left:220px; top:352px; width:619px;"></div>
    <div class="abs centered notice">If unable to keep this appointment,please contact<br>us as soon as possible</div>

    <div class="follow" aria-label="Social profiles">
      <span class="follow__item follow__item--a"><span class="sr">Pawnet</span></span>
      <span class="follow__item follow__item--b"><span class="sr">Petbook</span></span>
      <span class="follow__item follow__item--c"><span class="sr">Chirper</span></span>
    </div>
    <div class="follow__label">Folow Us</div>
  </section>

</main>
</body>
</html>
```